Real Estate Webpage Design

We have an existing website: verindaleestates.com.au
We focus customised service mainly on Property Management and second-hand property sales.
We are not entirely happy about the current design and layout can stay roughly the same as the back end coding is linked to a CRM system.
We would like to see the design are more reachable to our clients and appearing.
Please check our Website Design Draft for more details.

Industry/Entity Type

Real estate Agency

Number of Pages Required

5+ page

Font styles to use
Sans Serif

Colors

Designer to choose colors to be used in the design.

```html
<!DOCTYPE html>
<html lang="en">
<head>
<meta charset="utf-8">
<title>Verindale Estates – Find your dream home</title>
<link href="https://fonts.googleapis.com/css2?family=Nunito:wght@400;600;700;800&display=swap" rel="stylesheet">
<style>
:root{
  --navy:#10284a;
  --navy-soft:#1c3a63;
  --yellow:#f9b516;
  --ink:#1e2533;
  --muted:#6b7280;
  --line:#d9dde4;
  --white:#ffffff;
  --card:#ffffff;
}
*{box-sizing:border-box;margin:0;padding:0}
html,body{width:1200px;height:4036px;overflow:hidden}
body{font-family:"Nunito",Arial,sans-serif;color:var(--ink);background:var(--white);position:relative}
.abs{position:absolute}
.btn{display:inline-block;background:var(--yellow);color:var(--ink);font-weight:700;font-size:14px;border-radius:22px;padding:10px 26px;border:none}
.blob{position:absolute}

/* header / hero */
.hero{position:absolute;left:0;top:0;width:1200px;height:660px;overflow:hidden}
.hero-photo{position:absolute;inset:0;background:linear-gradient(180deg,#5d6a78 0%,#8c8f8c 40%,#a3a39b 60%,#4f6f7d 85%,#2e4a5a 100%)}
.hero-shade{position:absolute;inset:0;background:rgba(12,22,38,.45)}
.nav{position:absolute;top:0;left:0;width:1200px;height:50px;display:flex;align-items:center;padding:0 50px;color:var(--white);font-size:13px}
.brand{display:flex;align-items:center;gap:8px;font-weight:800;font-size:26px;color:var(--yellow)}
.brand .mark{width:26px;height:26px;background:var(--yellow);border-radius:4px}
.nav-links{display:flex;gap:34px;margin-left:auto;align-items:center;font-weight:600}
.nav-links .strong{font-weight:800}
.nav .btn{margin-left:28px;padding:8px 22px;font-size:13px}
.hero-title{position:absolute;top:180px;left:0;width:1200px;text-align:center;color:var(--white);font-size:58px;font-weight:800;line-height:1.15}
.hero-sub{position:absolute;top:378px;left:0;width:1200px;text-align:center;color:var(--white);font-size:17px}
.hero .btn{position:absolute;top:452px;left:512px;padding:9px 30px;font-size:14px}
.scroll-cue{position:absolute;top:620px;left:0;width:1200px;text-align:center;color:#dfe4ea;font-size:11px}

/* about */
.about{position:absolute;left:140px;top:784px;width:920px;height:296px;background:var(--navy);color:var(--white);padding:34px 40px;border-radius:4px}
.about h2{font-size:22px;font-weight:800;margin-bottom:12px}
.about p{font-size:15px;line-height:1.42;width:460px}
.about-photo{position:absolute;left:668px;top:732px;width:344px;height:300px;border-radius:6px;background:linear-gradient(160deg,#f1f1ee 0%,#d9dde0 45%,#2d5aa8 70%,#88aac8 100%);box-shadow:0 8px 20px rgba(0,0,0,.18)}

/* services */
.section-title{position:absolute;left:0;width:1200px;text-align:center;font-size:26px;font-weight:800;color:var(--ink)}
.service h3{font-size:26px;font-weight:800;margin-bottom:14px}
.service p{font-size:15px;line-height:1.45;color:#3b4250}
.service .btn{margin-top:26px}
.svc-photo{position:absolute;border-radius:8px;box-shadow:0 8px 20px rgba(0,0,0,.18)}

/* listings */
.tabs{position:absolute;top:2410px;left:0;width:1200px;display:flex;justify-content:center;gap:12px}
.tab{border:1px solid var(--line);border-radius:16px;padding:6px 18px;font-size:12px;font-weight:700;color:var(--ink);background:var(--white)}
.tab.active{background:var(--navy);color:var(--white);border-color:var(--navy)}
.listing{position:absolute;top:2472px;width:262px;height:296px;background:var(--card);border-radius:8px;box-shadow:0 4px 16px rgba(0,0,0,.14);overflow:hidden}
.listing .photo{height:170px;position:relative}
.listing .tag{position:absolute;top:10px;left:10px;background:#d8f1e0;color:#1e6b3a;font-size:10px;font-weight:700;border-radius:3px;padding:2px 8px}
.listing .icons{position:absolute;top:10px;right:10px;display:flex;gap:6px}
.listing .icons span{width:20px;height:20px;background:var(--white);border-radius:4px}
.listing .agent{position:absolute;bottom:10px;right:10px;background:var(--white);font-size:10px;padding:3px 8px;border-radius:12px;font-weight:600}
.listing .body{padding:10px 12px;font-size:11px}
.listing .row{display:flex;justify-content:space-between;align-items:baseline}
.listing .name{font-weight:800;font-size:13px}
.listing .price{font-weight:800;font-size:15px}
.listing .addr{color:var(--muted);font-size:10px;margin-top:2px}
.listing .feat{display:flex;gap:10px;margin-top:10px;font-weight:700}
.listing .meta{color:var(--muted);font-size:9px;text-align:right;margin-top:-14px}

/* contact */
.contact{position:absolute;left:140px;top:2952px;width:920px;height:380px;background:var(--navy);border-radius:4px;padding:40px 60px;color:var(--white)}
.contact h2{font-size:22px;font-weight:800;margin-bottom:34px}
.field{position:absolute;height:34px;border:1px solid #8093ae;border-radius:4px;color:#c7d0dd;font-size:12px;padding:9px 12px}
.contact .btn{position:absolute;left:426px;top:322px;padding:8px 26px;font-size:13px}

/* testimonials */
.sub{position:absolute;left:0;width:1200px;text-align:center;font-size:15px;color:#444b57}
.quote{position:absolute;top:3532px;width:262px;height:110px;background:var(--white);border-radius:6px;box-shadow:0 3px 12px rgba(0,0,0,.12);padding:16px 20px;font-size:11px;line-height:1.45;color:#5b6270;text-align:center}
.avatar{position:absolute;top:3722px;width:40px;height:40px;border-radius:50%;background:#b9c2cf}
.person{position:absolute;top:3772px;width:262px;text-align:center;font-size:12px;font-weight:700}
.arrow{position:absolute;top:3584px;width:26px;height:26px;border-radius:50%;background:var(--navy);display:flex;align-items:center;justify-content:center}

/* footer */
.footer{position:absolute;left:0;top:3832px;width:1200px;height:204px;background:var(--yellow);padding:34px 60px;color:var(--ink)}
.footer .brand{color:var(--white);font-size:30px}
.footer .brand .mark{background:var(--white)}
.footer .blurb{font-size:10px;width:230px;margin-top:12px;line-height:1.4}
.footer .copy{font-size:9px;margin-top:14px}
.fcol{position:absolute;top:34px;font-size:12px;line-height:1.55}
.fcol h4{font-size:13px;font-weight:800;margin-bottom:4px}
.socials{display:flex;gap:8px;margin-top:6px}
.socials span{width:28px;height:28px;border-radius:50%;border:2px solid var(--ink)}
</style>
</head>
<body>

<header class="hero">
  <div class="hero-photo" role="img" aria-label="Photo of a modern two-storey home with a pool at dusk"></div>
  <div class="hero-shade"></div>
  <nav class="nav">
    <div class="brand"><span class="mark"></span>Verindale</div>
    <div class="nav-links">
      <span>Home</span><span>About us ▾</span><span>Landlord ▾</span><span>Tenant ▾</span><span>Property Sales ▾</span><span class="strong">Make a switch</span>
    </div>
    <span class="btn">Appraisal now</span>
  </nav>
  <h1 class="hero-title">Find your dream home<br>with Verindale</h1>
  <p class="hero-sub">Your local real estate property group.</p>
  <span class="btn">Request a free appraisal</span>
  <div class="scroll-cue">Scroll down</div>
</header>

<svg class="blob" style="left:1010px;top:640px" width="190" height="110" viewBox="0 0 190 110"><path d="M30 60 C20 20 80 0 120 20 C160 35 190 10 190 10 L190 110 L60 110 C30 100 40 85 30 60Z" fill="var(--yellow)"/></svg>

<section class="about">
  <h2>Verindale – Spanish for "the home"</h2>
  <p>Buying a property is one of the most expensive expenses and important assets for people. Verindale is a real estate company located in Larkfield, Canberra.<br>Being a portfolio sales agent and property manager, coupled with our high-profile international real estate experience, Verindale is considered a market leader on the cutting edge with deep industry knowledge, ranging from landlord–tenant relationship, residential purchases.</p>
</section>
<div class="about-photo" role="img" aria-label="Photo of a white house with a blue door beside a pool"></div>

<h2 class="section-title" style="top:1236px">Our services</h2>

<svg class="blob" style="left:60px;top:1640px" width="130" height="90" viewBox="0 0 130 90"><path d="M10 50 C0 10 60 0 90 15 C125 30 130 70 95 82 C60 95 20 90 10 50Z" fill="var(--navy)"/></svg>
<svg class="blob" style="left:40px;top:1690px" width="60" height="50" viewBox="0 0 60 50"><path d="M5 25 C5 5 40 0 52 15 C62 30 45 48 25 45 C10 43 5 35 5 25Z" fill="var(--yellow)"/></svg>

<div class="service abs" style="left:140px;top:1462px;width:460px">
  <h3>Property Management</h3>
  <p>This paragraph here will elaborate this service further. Verindale Property group can manage your properties for you at an affordable rate. Contact us today to get started with us for your better future.</p>
  <span class="btn">Appraisal now</span>
</div>
<div class="svc-photo" style="left:670px;top:1372px;width:342px;height:296px;background:linear-gradient(150deg,#3a3a3a 0%,#7b7b7b 40%,#cfcfcf 75%,#e8e8e8 100%)" role="img" aria-label="Photo of people working on a laptop at a desk"></div>

<svg class="blob" style="left:1050px;top:1690px" width="150" height="120" viewBox="0 0 150 120"><path d="M40 20 C80 -5 150 10 150 10 L150 110 C110 125 60 110 30 90 C5 70 10 35 40 20Z" fill="var(--navy)"/></svg>

<div class="svc-photo" style="left:140px;top:1844px;width:350px;height:400px;background:linear-gradient(180deg,#c9d6c4 0%,#9fb48f 45%,#6e8f4f 75%,#4f7a35 100%)" role="img" aria-label="Photo of a green suburban house with a stepping-stone path"></div>
<div class="service abs" style="left:550px;top:1936px;width:470px">
  <h3>Property Sales</h3>
  <p>This paragraph here will elaborate this service further. Verindale Property group can manage your properties for you at an affordable rate. Contact us today to get started with us for your better future.</p>
  <span class="btn">Appraisal now</span>
</div>

<h2 class="section-title" style="top:2344px">Property of the week</h2>
<div class="tabs"><span class="tab active">For Sale</span><span class="tab">For Lease</span><span class="tab">Sold</span><span class="tab">Leased</span></div>

<article class="listing" style="left:184px">
  <div class="photo" role="img" aria-label="Photo of a modern dark townhouse" style="background:linear-gradient(160deg,#bcd3e8 0%,#8ea6bd 50%,#3d4d5e 100%)"><span class="tag">For Sale</span><div class="icons"><span></span><span></span></div><span class="agent">Contact agent</span></div>
  <div class="body"><div class="row"><span class="name">Townhouse in 4th</span><span class="price">$ 742,000</span></div><div class="addr">Lot 12, Riverbend Way, Larkfield</div><div class="feat"><span>4 ▪</span><span>2 ▪</span><span>2 ▪</span></div><div class="meta">List: 04 Mar 2023<br>$820,000 – $842,000</div></div>
</article>
<article class="listing" style="left:469px">
  <div class="photo" role="img" aria-label="Photo of a brick family home with garden" style="background:linear-gradient(160deg,#cfe0ef 0%,#a7b59a 55%,#5f6f4c 100%)"><span class="tag">For Sale</span><div class="icons"><span></span><span></span></div><span class="agent">Contact agent</span></div>
  <div class="body"><div class="row"><span class="name">Townhouse in 4th</span><span class="price">$ 742,000</span></div><div class="addr">Lot 18, Harbour Street, Larkfield</div><div class="feat"><span>4 ▪</span><span>2 ▪</span><span>2 ▪</span></div><div class="meta">List: 04 Mar 2023<br>$820,000 – $842,000</div></div>
</article>
<article class="listing" style="left:754px">
  <div class="photo" role="img" aria-label="Photo of a white weatherboard house" style="background:linear-gradient(160deg,#d5e4f1 0%,#b9c1c6 55%,#6f8a5b 100%)"><span class="tag">For Sale</span><div class="icons"><span></span><span></span></div><span class="agent">Contact agent</span></div>
  <div class="body"><div class="row"><span class="name">Townhouse in 4th</span><span class="price">$ 742,000</span></div><div class="addr">Lot 21, Elm Crescent, Larkfield</div><div class="feat"><span>4 ▪</span><span>2 ▪</span><span>2 ▪</span></div><div class="meta">List: 04 Mar 2023<br>$820,000 – $842,000</div></div>
</article>

<span class="btn abs" style="left:541px;top:2830px;padding:8px 26px;font-size:13px">View more</span>

<svg class="blob" style="left:1020px;top:2660px" width="180" height="220" viewBox="0 0 180 220"><path d="M50 30 C90 -5 180 10 180 10 L180 210 C130 225 70 200 40 160 C5 115 10 65 50 30Z" fill="var(--yellow)"/></svg>

<section class="contact">
  <h2>Get in touch with us</h2>
  <div class="field" style="left:60px;top:106px;width:390px">First name</div>
  <div class="field" style="left:470px;top:106px;width:390px">Surname</div>
  <div class="field" style="left:60px;top:152px;width:390px">Phone number</div>
  <div class="field" style="left:470px;top:152px;width:390px">Email</div>
  <div class="field" style="left:60px;top:198px;width:800px;height:80px">Message</div>
  <span class="btn">Send</span>
</section>

<svg class="blob" style="left:0;top:3600px" width="100" height="150" viewBox="0 0 100 150"><path d="M0 10 C40 0 90 30 95 75 C100 120 60 150 0 145Z" fill="var(--navy)"/></svg>

<h2 class="section-title" style="top:3416px">Testimonials</h2>
<p class="sub" style="top:3470px">Read what our clients say about us</p>

<div class="arrow" style="left:50px"><svg width="12" height="12" viewBox="0 0 12 12"><path d="M8 2 L4 6 L8 10" stroke="#fff" stroke-width="2" fill="none"/></svg></div>
<div class="arrow" style="left:1124px"><svg width="12" height="12" viewBox="0 0 12 12"><path d="M4 2 L8 6 L4 10" stroke="#fff" stroke-width="2" fill="none"/></svg></div>

<div class="quote" style="left:184px">Verindale is the best property manager! Always happy to respond to my queries and keep us well informed at all stage. I will definitely recommend her to my friends.</div>
<div class="quote" style="left:469px">Verindale is the best property manager! Always happy to respond to my queries and keep us well informed at all stage. I will definitely recommend her to my friends.</div>
<div class="quote" style="left:754px">Verindale is the best property manager! Always happy to respond to my queries and keep us well informed at all stage. I will definitely recommend her to my friends.</div>
<div class="avatar" style="left:295px" role="img" aria-label="Client portrait"></div>
<div class="avatar" style="left:580px" role="img" aria-label="Client portrait"></div>
<div class="avatar" style="left:865px" role="img" aria-label="Client portrait"></div>
<div class="person" style="left:184px">Owen Hartley</div>
<div class="person" style="left:469px">Marcus Ellery</div>
<div class="person" style="left:754px">Bianca Rowe</div>

<footer class="footer">
  <div class="brand"><span class="mark"></span>Verindale</div>
  <p class="blurb">Buying a property is one of the most expensive expenses and important assets for people. Verindale is a real estate company located in Larkfield, Canberra.</p>
  <p class="copy">© All rights reserved 2023</p>
  <div class="fcol" style="left:390px"><h4>Sitemap</h4>Home<br>About us<br>Services<br>Buy now<br>Blog<br>Contact us</div>
  <div class="fcol" style="left:528px"><h4>Useful links</h4>Privacy policy<br>Complaints handling &amp;<br>Dispute resolution<br>Due diligence checklist</div>
  <div class="fcol" style="left:690px"><h4>Contact us</h4>14/3 Quarry Lane,<br>Larkfield ACT 2915<br>02 6100 4826<br>hello@verindaleestates.com.au<br>Monday – Friday<br>9.00 am – 5.00pm</div>
  <div class="fcol" style="left:906px"><h4>Follow us</h4><div class="socials"><span></span><span></span><span></span><span></span></div></div>
</footer>

</body>
</html>
```